political campaign tax exemption on school taxes that dont have kids in the district

Velmora School Board Races

Taxes, Taxes, Taxes!
Everyone pays them!
You have tax exemption for the elderly.
You have tax exemption for the veterans.
What about tax exemptions for you?

In Texas, a governing entity, has the option of giving a 20 percent tax exemption. Our current school board, hasnt offered it you! We will!

Can we count on your vote? You can count on ours!
small discloure (political ad paid by candidates)

attached are the candidates for this exemption

Political

• need to include disclaimer at bottom.

political ad paid by candidate

```html
<!DOCTYPE html>
<html lang="en">
<head>
<meta charset="utf-8">
<title>Taxes, Taxes, Taxes! — Velmora School Board Races</title>
<link rel="stylesheet" href="https://fonts.googleapis.com/css2?family=Bebas+Neue&display=swap">
<style>
  :root {
    --ink: #1d1d1b;
    --sky: #1f9fd8;
    --sky-light: #43a3d6;
    --white: #ffffff;
    --accent: #73c6ef;
    --muted: #b9b9b4;
  }
  html, body {
    margin: 0;
    padding: 0;
    width: 1200px;
    height: 926px;
    overflow: hidden;
    background: var(--ink);
  }
  .flyer {
    position: relative;
    width: 1200px;
    height: 926px;
    background: var(--ink);
    font-family: "Bebas Neue", "Arial Narrow", sans-serif;
    color: var(--white);
    overflow: hidden;
  }
  .sky {
    position: absolute;
    inset: 0;
    width: 1200px;
    height: 926px;
  }
  .illustration {
    position: absolute;
    left: 783px;
    top: 63px;
    width: 392px;
    height: 385px;
    background: linear-gradient(160deg, #f4f4f4 0%, #f4f4f4 30%, #2a2a28 60%, #1d1d1b 100%);
    border-radius: 4px;
    opacity: 0.9;
  }
  .headline {
    position: absolute;
    margin: 0;
    font-weight: 400;
    font-size: 134px;
    line-height: 1;
    letter-spacing: 1px;
    white-space: nowrap;
  }
  .headline--one { left: 60px; top: 23px; }
  .headline--two { left: 154px; top: 147px; }
  .headline--three { left: 230px; top: 258px; }
  .points {
    position: absolute;
    left: 63px;
    top: 400px;
    margin: 0;
    padding: 0;
    list-style: none;
    font-size: 41px;
    line-height: 33px;
    white-space: nowrap;
  }
  .question {
    position: absolute;
    left: 62px;
    top: 502px;
    margin: 0;
    font-size: 64px;
    line-height: 1;
    white-space: nowrap;
  }
  .call-to-vote {
    position: absolute;
    left: 62px;
    top: 644px;
    margin: 0;
    font-size: 62px;
    line-height: 1;
    color: var(--accent);
    white-space: nowrap;
  }
  .promise {
    position: absolute;
    left: 62px;
    top: 734px;
    margin: 0;
    font-size: 38px;
    line-height: 30px;
    white-space: nowrap;
  }
  .race {
    position: absolute;
    left: 63px;
    top: 848px;
    margin: 0;
    font-size: 30px;
    line-height: 1;
    color: var(--accent);
    white-space: nowrap;
  }
  .disclaimer {
    position: absolute;
    left: 63px;
    top: 888px;
    margin: 0;
    font-size: 20px;
    line-height: 1;
    letter-spacing: 0.5px;
    color: var(--muted);
    white-space: nowrap;
  }
</style>
</head>
<body>
<main class="flyer">
  <svg class="sky" viewBox="0 0 1200 926" aria-hidden="true">
    <polygon fill="var(--sky)" points="373,0 720,0 720,335 690,315 620,250 540,160 450,70"/>
    <polygon fill="var(--sky-light)" points="720,0 1200,0 1200,461 1100,445 1000,430 900,415 800,395 720,335"/>
  </svg>

  <div class="illustration" role="img" aria-label="Two businessmen in silhouette straining to carry a giant TAX sign uphill"></div>

  <h1 class="headline headline--one">Taxes,</h1>
  <p class="headline headline--two">Taxes,</p>
  <p class="headline headline--three">Taxes!</p>

  <ul class="points">
    <li>Everyone pays them!</li>
    <li>You have tax exemption for the elderly.</li>
    <li>You have tax exemption for the veterans</li>
  </ul>

  <p class="question">What about tax exemptions for you?</p>

  <p class="call-to-vote">Can we count on your vote? You can count on ours!</p>

  <p class="promise">In Texas, a governing entity, has the option of giving<br>
  a 20 percent tax exemption. Our current school board,<br>
  hasnt offered it you! We will!</p>

  <p class="race">Velmora School Board Races</p>
  <p class="disclaimer">Political ad paid for by the candidates</p>
</main>
</body>
</html>
```